Field Tracking Guide: Seizures

Book cover. Casebound and Perfect bound. Size 5.5 x 8.5 (portrait). Approx 165 pages for spine. Will be using Velmora PressWorks for printer so be sure to follow those specifications. This is a textbook for Search & Rescue and Law Enforcement search planners on deciding where they should look for someone who has been abducted. Nothing morbid. It will be a book in a series. The series is called Field Tracking Guide. That should be in smaller letters at the top. Abductions should be the major title feature. The series will have a border on the front cover of safety orange (255, 121, 0) for RGB. qxR logo on front, spine, and back. Place holder for ISBN, author bio, book description, endorsements on back.

Target Market(s)

Professional textbook for Law Enforcement, Search and Rescue, Academic (criminologist)

Industry/Entity Type

Search and Rescue - Law Enforcement. Major colors for industry is orange for SAR and blue for Law enforcement

Requirements
Must have
• Safety Orange border (0.25 inch), qxR Logos, small Field Tracking Guide title on top, large Abductions title. Author's name (Daniel P. Wirthman)
Nice to have
• Not sure if picture or illustration works best. Topographic map is possible, law enforcement and searcher working together, clandestine grave, dirt road, all possible
Should not have
• no dead bodies, no bones, no skulls, no urban environment

```html
<!DOCTYPE html>
<html lang="en">
<head>
<meta charset="utf-8">
<title>Field Tracking Guide: Seizures — Cover Wraps</title>
<link rel="stylesheet" href="https://fonts.googleapis.com/css2?family=Bebas+Neue&family=Source+Sans+3:wght@400;600&family=Arimo:wght@400&display=swap">
<style>
  :root {
    --paper: #f1f1f1;
    --navy: #2e3866;
    --navy-mid: #3a4578;
    --navy-deep: #1a2247;
    --navy-ink: #0c1130;
    --spine: #2a3460;
    --safety-orange: #ff7900;
    --ink-light: #ecebe8;
    --ink-soft: #dcdeea;
    --placeholder: #e6e6e6;
    --placeholder-text: #a9a9a9;
    --logo-bg: #ffffff;
    --logo-ink: #1b1b1b;
    --logo-rule: #d2461e;
  }
  * { box-sizing: border-box; margin: 0; padding: 0; }
  html, body { width: 800px; height: 1200px; overflow: hidden; }
  body {
    background: var(--paper);
    font-family: "Arimo", Arial, sans-serif;
    position: relative;
  }

  .wrap {
    position: absolute;
    left: 86px;
    width: 630px;
    height: 446px;
    display: grid;
    grid-template-columns: 292px 46px 292px;
  }
  .wrap--series-border { top: 77px; }
  .wrap--plain { top: 634px; }

  .panel {
    position: relative;
    overflow: hidden;
    background: linear-gradient(180deg, var(--navy-mid) 0%, var(--navy) 55%, var(--navy-deep) 100%);
  }
  .wrap--series-border .panel--back,
  .wrap--series-border .panel--front {
    border: 12px solid var(--safety-orange);
  }

  .ridge {
    position: absolute;
    left: 0; right: 0; top: 0;
    height: 50px;
    background: linear-gradient(180deg, var(--navy-ink) 0%, var(--navy-deep) 75%, rgba(26,34,71,0) 100%);
  }
  .ground {
    position: absolute;
    left: 0; right: 0; bottom: 0;
    height: 56px;
    background: linear-gradient(180deg, rgba(12,17,48,0) 0%, var(--navy-ink) 55%);
  }

  /* Back cover */
  .back-photo {
    position: absolute;
    left: 10px; top: 64px;
    width: 61px; height: 78px;
    background: var(--placeholder);
  }
  .back-heading {
    position: absolute;
    left: 83px; top: 54px;
    color: var(--ink-light);
  }
  .back-heading .title {
    font-family: "Bebas Neue", "Oswald", sans-serif;
    font-weight: 400;
    font-size: 27px;
    line-height: 0.95;
    letter-spacing: 0.3px;
  }
  .back-heading .series {
    font-family: "Source Sans 3", sans-serif;
    font-size: 9px;
    letter-spacing: 0.2px;
  }
  .back-copy {
    position: absolute;
    color: var(--ink-soft);
    font-size: 6.6px;
    line-height: 8.5px;
    text-align: justify;
    hyphens: auto;
  }
  .back-copy p + p { margin-top: 8.5px; }
  .back-copy--lead { left: 83px; right: 8px; top: 95px; }
  .back-copy--body { left: 5px; right: 8px; top: 164px; }
  .endorsements {
    position: absolute;
    left: 5px; right: 8px; top: 330px; height: 26px;
  }

  .logo {
    display: flex;
    align-items: center;
    justify-content: center;
    gap: 2px;
    background: var(--logo-bg);
    color: var(--logo-ink);
    font-family: "Source Sans 3", sans-serif;
    font-weight: 600;
  }
  .logo-mark {
    width: 4px; height: 4px;
    background: var(--logo-rule);
  }
  .panel--back .logo {
    position: absolute;
    left: 10px; bottom: 14px;
    width: 42px; height: 34px;
    font-size: 16px;
    letter-spacing: -0.5px;
    z-index: 2;
  }
  .isbn-box {
    position: absolute;
    right: 10px; bottom: 12px;
    width: 96px; height: 48px;
    background: var(--placeholder);
    color: var(--placeholder-text);
    font-family: "Source Sans 3", sans-serif;
    font-size: 15px;
    letter-spacing: 4px;
    display: flex; align-items: center; justify-content: center;
    z-index: 2;
  }

  /* Spine */
  .spine {
    position: relative;
    background: var(--spine);
    color: var(--ink-light);
    display: flex;
    flex-direction: column;
    align-items: center;
    padding-top: 20px;
  }
  .spine-title {
    writing-mode: vertical-rl;
    font-family: "Bebas Neue", "Oswald", sans-serif;
    font-size: 26px;
    letter-spacing: 0.3px;
    line-height: 1;
  }
  .spine-series {
    writing-mode: vertical-rl;
    margin-top: 50px;
    font-family: "Source Sans 3", sans-serif;
    font-size: 11px;
    letter-spacing: 0.5px;
  }
  .spine .logo {
    position: absolute;
    bottom: 14px;
    left: 6px;
    width: 34px; height: 42px;
    writing-mode: vertical-rl;
    font-size: 15px;
  }

  /* Front cover */
  .front-series {
    position: absolute;
    left: 0; right: 0; top: 80px;
    display: flex; align-items: center; justify-content: center;
    gap: 6px;
    color: var(--ink-light);
    font-family: "Source Sans 3", sans-serif;
    font-size: 8px;
    letter-spacing: 0.2px;
  }
  .front-series::before, .front-series::after {
    content: "";
    width: 40px; height: 1px;
    background: var(--ink-light);
  }
  .front-title {
    position: absolute;
    left: 0; right: 0; top: 88px;
    text-align: center;
    font-family: "Bebas Neue", "Oswald", sans-serif;
    font-weight: 400;
    font-size: 68px;
    line-height: 1;
    letter-spacing: 1px;
    color: var(--ink-light);
  }
  .wrap--series-border .front-title { color: var(--safety-orange); }
  .front-subtitle {
    position: absolute;
    left: 0; right: 0; top: 151px;
    text-align: center;
    font-family: "Source Sans 3", sans-serif;
    font-size: 8px;
    line-height: 10.5px;
    color: var(--ink-light);
  }
  .front-scene {
    position: absolute;
    left: 0; right: 0; top: 196px; bottom: 0;
    background:
      linear-gradient(150deg, rgba(200,208,238,0) 30%, rgba(200,208,238,0.28) 42%, rgba(200,208,238,0) 56%),
      linear-gradient(180deg, #232c57 0%, var(--navy-deep) 35%, #141a3c 65%, var(--navy-ink) 100%);
  }
  .front-author {
    position: absolute;
    left: 0; right: 0; bottom: 10px;
    text-align: center;
    font-family: "Source Sans 3", sans-serif;
    font-size: 13.5px;
    letter-spacing: 3px;
    color: var(--ink-light);
  }
</style>
</head>
<body>

<section class="wrap wrap--series-border" aria-label="Cover wrap with safety orange series border">
  <article class="panel panel--back">
    <div class="ridge" role="img" aria-label="Dark mountain ridge silhouette"></div>
    <div class="back-photo" aria-label="Author photo placeholder"></div>
    <header class="back-heading">
      <h2 class="title">SEIZURES</h2>
      <p class="series">FIELD TRACKING GUIDE</p>
    </header>
    <div class="back-copy back-copy--lead">
      <p>When a person is taken against their will, every decision made in the first hours can determine the outcome. Seizures delivers a structured, evidence-based approach for search planners, law enforcement professionals, and rescue teams tasked with locating abducted individuals.</p>
    </div>
    <div class="back-copy back-copy--body">
      <p>Drawing from real-world case analysis, behavioral patterns, and search theory, this book bridges the gap between investigation and field operations. It provides actionable insights into offender behavior, victim movement, and geographic profiling—allowing teams to prioritize search areas with greater precision and efficiency.</p>
      <p>Designed as part of the Field Tracking Guide series, this volume integrates proven methodologies with practical tools to support coordinated response efforts. Whether operating in rural terrain or complex environments, professionals will gain a clearer understanding of where to search, why those locations matter, and how to allocate resources effectively.</p>
      <p>This is not speculation—it is a disciplined framework built for those responsible for bringing people home.</p>
      <p>About the Author<br>Daniel P. Wirthman is a recognized authority in search and rescue planning, with decades of experience analyzing lost person incidents and developing behavior-based search strategies used worldwide.</p>
    </div>
    <div class="endorsements" aria-label="Space reserved for endorsements"></div>
    <div class="ground" role="img" aria-label="Dark hillside silhouette"></div>
    <div class="logo"><span>qxR</span><span class="logo-mark"></span></div>
    <div class="isbn-box">ISBN</div>
  </article>

  <aside class="spine">
    <span class="spine-title">SEIZURES</span>
    <span class="spine-series">FIELD TRACKING GUIDE</span>
    <div class="logo"><span>qxR</span></div>
  </aside>

  <article class="panel panel--front">
    <div class="ridge" role="img" aria-label="Dark mountain ridge silhouette"></div>
    <div class="front-scene" role="img" aria-label="Illustration: silhouetted officer with flashlight and a searcher kneeling by disturbed ground in tall grass"></div>
    <p class="front-series">FIELD TRACKING GUIDE</p>
    <h1 class="front-title">SEIZURES</h1>
    <p class="front-subtitle">SEARCH &amp; RESCUE AND LAW ENFORCEMENT<br>PLANNING GUIDE</p>
    <p class="front-author">Daniel P. Wirthman</p>
  </article>
</section>

<section class="wrap wrap--plain" aria-label="Cover wrap without border">
  <article class="panel panel--back">
    <div class="ridge" role="img" aria-label="Dark mountain ridge silhouette"></div>
    <div class="back-photo" aria-label="Author photo placeholder"></div>
    <header class="back-heading">
      <h2 class="title">SEIZURES</h2>
      <p class="series">FIELD TRACKING GUIDE</p>
    </header>
    <div class="back-copy back-copy--lead">
      <p>When a person is taken against their will, every decision made in the first hours can determine the outcome. Seizures delivers a structured, evidence-based approach for search planners, law enforcement professionals, and rescue teams tasked with locating abducted individuals.</p>
    </div>
    <div class="back-copy back-copy--body">
      <p>Drawing from real-world case analysis, behavioral patterns, and search theory, this book bridges the gap between investigation and field operations. It provides actionable insights into offender behavior, victim movement, and geographic profiling—allowing teams to prioritize search areas with greater precision and efficiency.</p>
      <p>Designed as part of the Field Tracking Guide series, this volume integrates proven methodologies with practical tools to support coordinated response efforts. Whether operating in rural terrain or complex environments, professionals will gain a clearer understanding of where to search, why those locations matter, and how to allocate resources effectively.</p>
      <p>This is not speculation—it is a disciplined framework built for those responsible for bringing people home.</p>
      <p>About the Author<br>Daniel P. Wirthman is a recognized authority in search and rescue planning, with decades of experience analyzing lost person incidents and developing behavior-based search strategies used worldwide.</p>
    </div>
    <div class="endorsements" aria-label="Space reserved for endorsements"></div>
    <div class="ground" role="img" aria-label="Dark hillside silhouette"></div>
    <div class="logo"><span>qxR</span><span class="logo-mark"></span></div>
    <div class="isbn-box">ISBN</div>
  </article>

  <aside class="spine">
    <span class="spine-title">SEIZURES</span>
    <span class="spine-series">FIELD TRACKING GUIDE</span>
    <div class="logo"><span>qxR</span></div>
  </aside>

  <article class="panel panel--front">
    <div class="ridge" role="img" aria-label="Dark mountain ridge silhouette"></div>
    <div class="front-scene" role="img" aria-label="Illustration: silhouetted officer with flashlight and a searcher kneeling by disturbed ground in tall grass"></div>
    <p class="front-series">FIELD TRACKING GUIDE</p>
    <h1 class="front-title">SEIZURES</h1>
    <p class="front-subtitle">SEARCH &amp; RESCUE AND LAW ENFORCEMENT<br>PLANNING GUIDE</p>
    <p class="front-author">Daniel P. Wirthman</p>
  </article>
</section>

</body>
</html>
```